MARLOW CREST WINE LABEL DESIGN PROJECT

We need an elegant wine label design for our new range of wine. We need 3 labels for the range

2015 MARLOW CREST SHIRAZ
2015 MARLOW CREST CABERNET SAUVIGNON
2015 MARLOW CREST CABERNET SHIRAZ

The Size is nominated at 120mm High x 90mm Wide (Front and Back) but we are open to creative expression even if size differs

We are open to any style of label and designer can work on their strengths. it can be modern/classic/old fashion etc

I have attached the marlow crest logo ( the 2 olives) and a set up called wine mandatories which is in no way a design direction just the mandatory info that needs to appear on labels. The wine mandatories is just the information that needs to go on the label it has nothing to do with the design. DO not make designs based on this at all. These labels are for red wine not olive oil.

I have also attached some of the companies current olive oil labels ( TORQUALE AND WANDELLA AND MARLOW CREST so you can see other labels and how this wine product will sit in gift baskets.

Thanks
Tomasz.

Reason: Hello Friends We have decided to extend the deadline to enable more submissions. Many of the designs submitted have images of olives and look like olive oil product. We only need the olive logo to be shown on the label but the rest of the design should be a classic simple red wine label. It is not olive oil or olive product - it is red wine. Please keep simple and stylish Thanks Tomasz

Target Market(s)

35-65

Font styles to use
Serif

Requirements
Must have
• AS per brief
Nice to have
• as per brief
Should not have
• as per brief

```html
<!DOCTYPE html>
<html lang="en">
<head>
<meta charset="utf-8">
<title>Marlow Crest – Cabernet Sauvignon 2015 Labels</title>
<link rel="stylesheet" href="https://fonts.googleapis.com/css2?family=Cinzel:wght@400;700&display=swap">
<style>
  :root {
    --ring-green: #8cc63f;
    --ring-gold: #c9973a;
    --ring-cream: #f4e6c0;
    --ink: #111111;
    --rule-green: #8cc63f;
    --mark-dark: #2a1a22;
    --box-line: #111111;
    --silver-light: #ffffff;
    --silver-edge: #dcdde0;
    --gold-light: #fbf3d9;
    --gold-mid: #d9b45a;
    --gold-edge: #b38a2c;
    --page: #ffffff;
  }
  html, body {
    margin: 0;
    padding: 0;
    width: 1200px;
    height: 1182px;
    overflow: hidden;
    background: var(--page);
  }
  .label-sheet {
    display: block;
    width: 1200px;
    height: 1182px;
  }
  .ring-outer { fill: var(--ring-green); }
  .ring-gold { fill: var(--ring-gold); }
  .ring-cream { fill: var(--ring-cream); }
  .face-silver { fill: url(#silverFace); }
  .face-gold { fill: url(#goldFace); }
  .label-text {
    font-family: "Cinzel", serif;
    fill: var(--ink);
  }
  .arc-tagline { font-size: 21px; letter-spacing: 5px; }
  .arc-volume { font-size: 18px; letter-spacing: 1px; }
  .arc-drinks { font-size: 14px; letter-spacing: 0.5px; }
  .wordmark-large { font-size: 25px; font-weight: 700; letter-spacing: 4px; }
  .wordmark-small { font-size: 12px; font-weight: 700; letter-spacing: 2.5px; }
  .varietal { font-size: 23px; letter-spacing: 0.5px; }
  .producer { font-size: 16px; letter-spacing: 0.5px; }
  .brand-dot { fill: var(--mark-dark); }
  .rule { stroke: var(--rule-green); stroke-width: 1.2; }
  .mandatory-box { fill: none; stroke: var(--box-line); stroke-width: 2; }
</style>
</head>
<body>
<svg class="label-sheet" viewBox="0 0 1200 1182" xmlns="http://www.w3.org/2000/svg">
  <defs>
    <radialGradient id="silverFace" cx="50%" cy="50%" r="50%">
      <stop offset="0%" stop-color="var(--silver-light)"/>
      <stop offset="75%" stop-color="#f1f1f2"/>
      <stop offset="100%" stop-color="var(--silver-edge)"/>
    </radialGradient>
    <radialGradient id="goldFace" cx="52%" cy="50%" r="55%">
      <stop offset="0%" stop-color="var(--gold-light)"/>
      <stop offset="45%" stop-color="var(--gold-mid)"/>
      <stop offset="100%" stop-color="var(--gold-edge)"/>
    </radialGradient>
    <path id="arcTop" d="M -200,0 A 200 200 0 0 1 200,0"/>
    <path id="arcBottom" d="M -200,0 A 200 200 0 0 0 200,0"/>
    <path id="arcBottomWide" d="M -212,0 A 212 212 0 0 0 212,0"/>

    <g id="labelRings">
      <circle class="ring-outer" r="272"/>
      <circle class="ring-cream" r="257"/>
      <circle class="ring-gold" r="254"/>
      <circle class="ring-cream" r="251"/>
      <circle class="ring-gold" r="249"/>
    </g>

    <g id="frontContent">
      <text class="label-text arc-tagline"><textPath href="#arcTop" startOffset="50%" text-anchor="middle">PREMIUM AUSTRALIAN WINE</textPath></text>
      <circle class="brand-dot" cx="0" cy="-85" r="42"/>
      <text class="label-text wordmark-large" x="0" y="58" text-anchor="middle" textLength="336" lengthAdjust="spacing">THE MARLOW CREST</text>
      <line class="rule" x1="-168" y1="81" x2="172" y2="81"/>
      <text class="label-text varietal" x="0" y="116" text-anchor="middle">CABERNET SAUVIGNON 2015</text>
      <text class="label-text arc-volume"><textPath href="#arcBottom" startOffset="50%" text-anchor="middle">14.5% ALC/VOL   750 ML</textPath></text>
    </g>

    <g id="backContent">
      <circle class="brand-dot" cx="0" cy="-177" r="26"/>
      <text class="label-text wordmark-small" x="0" y="-116" text-anchor="middle">THE MARLOW CREST</text>
      <line class="rule" x1="-170" y1="-102" x2="170" y2="-102"/>
      <text class="label-text varietal" x="0" y="-76" text-anchor="middle">CABERNET SAUVIGNON 2015</text>
      <text class="label-text producer" text-anchor="middle">
        <tspan x="0" y="-21">Produced by:</tspan>
        <tspan x="0" y="-2">The Marlow Crest Company</tspan>
        <tspan x="0" y="17">14 Ferrow Lane</tspan>
        <tspan x="0" y="36">Kelby Ridge</tspan>
        <tspan x="0" y="55">South Australia 5399</tspan>
      </text>
      <rect class="mandatory-box" x="-70" y="96" width="142" height="68"/>
      <text class="label-text arc-drinks"><textPath href="#arcBottomWide" startOffset="50%" text-anchor="middle">14.5% ALC/VOL Approx. 8.3 Standard Drinks</textPath></text>
    </g>
  </defs>

  <g class="label front-silver" transform="translate(314 314)">
    <use href="#labelRings"/>
    <circle class="face-silver" r="246"/>
    <use href="#frontContent"/>
  </g>

  <g class="label back-silver" transform="translate(884 314)">
    <use href="#labelRings"/>
    <circle class="face-silver" r="246"/>
    <use href="#backContent"/>
  </g>

  <g class="label front-gold" transform="translate(314 868)">
    <use href="#labelRings"/>
    <circle class="face-gold" r="246"/>
    <use href="#frontContent"/>
  </g>

  <g class="label back-gold" transform="translate(884 868)">
    <use href="#labelRings"/>
    <circle class="face-gold" r="246"/>
    <use href="#backContent"/>
  </g>
</svg>
</body>
</html>
```